CM Candle Tube Packaging Design

Website: www.corvelmarin.example
IG: @corvel.marin
Tagline: Elevate Your Ambiance
My brand is a sophisticated brand with luxury candles made of coconut wax. Im looking for an upscale minimalist chic design.
Discover the transformative power of positive energy with Corvel Marin candles. Indulge in true luxury with our specially crafted coconut wax blend that not only ignites captivating scents but also embodies modern elegance and empowering elements.
At Corvel Marin we're committed to delivering a unique and exhilarating aromatic experience to all candle lovers. Each candle is meticulously handcrafted in small batches using luxury fragrance oils exclusively formulated for coconut wax.
Our candles are:
Clean-burning
Paraben-Free
Phthalate-Free
Skin-Safe
Pet-Friendly
Look and feel

```html
<!DOCTYPE html>
<html lang="en">
<head>
<meta charset="UTF-8">
<title>Corvel Marin — Candle Tube Label</title>
<link rel="stylesheet" href="https://fonts.googleapis.com/css2?family=Italiana&family=Marcellus&display=swap">
<style>
  :root {
    --backdrop: #f3dcd2;
    --label: #f8e1dd;
    --label-edge: #e6c6c0;
    --panel: #e9b9b6;
    --panel-ink: #fbe8e5;
    --wordmark: #e8bcb7;
    --claims: #6e6a6a;
  }
  * { box-sizing: border-box; margin: 0; padding: 0; }
  html, body {
    width: 1200px;
    height: 723px;
    overflow: hidden;
    background: var(--backdrop);
  }
  .canvas {
    position: relative;
    width: 1200px;
    height: 723px;
  }
  .label {
    position: absolute;
    left: 400px;
    top: 30px;
    width: 400px;
    height: 664px;
    overflow: hidden;
    background: var(--label);
    border: 1px solid var(--label-edge);
    box-shadow: 2px 3px 8px rgba(120, 80, 70, 0.25);
  }
  .tagline-panel {
    position: absolute;
    left: 104px;
    top: 241px;
    width: 127px;
    height: 176px;
    background: var(--panel);
    color: var(--panel-ink);
    text-align: center;
  }
  .tagline-panel__name {
    margin-top: 28px;
    font-family: "Italiana", serif;
    font-size: 40px;
    line-height: 1;
    letter-spacing: 1px;
  }
  .tagline-panel__text {
    margin-top: 30px;
    font-family: "Marcellus", serif;
    font-size: 24px;
    line-height: 19px;
  }
  .wordmark {
    position: absolute;
    right: 40px;
    bottom: 100px;
    height: 520px;
    writing-mode: vertical-rl;
    transform: rotate(180deg);
    font-family: "Italiana", serif;
    font-size: 70px;
    line-height: 1;
    letter-spacing: 4px;
    text-align: center;
    color: var(--wordmark);
    white-space: nowrap;
  }
  .claims {
    position: absolute;
    left: 0;
    right: 0;
    top: 604px;
    text-align: center;
    font-family: "Marcellus", serif;
    font-size: 15px;
    line-height: 19px;
    color: var(--claims);
  }
  .claims span { margin: 0 4px; }
</style>
</head>
<body>
  <main class="canvas">
    <section class="label">
      <div class="tagline-panel">
        <p class="tagline-panel__name">CM</p>
        <p class="tagline-panel__text">Elevate<br>your<br>Ambiance</p>
      </div>
      <h1 class="wordmark">CORVEL MARIN</h1>
      <div class="claims">
        <p><span>• Clean Burning</span><span>• Paraben Free</span><span>• Phthalate Free</span></p>
        <p><span>• Skin Safe</span><span>• Pet Friendly</span></p>
      </div>
    </section>
  </main>
</body>
</html>
```